Ironleaf Personal Training Studio Information Card

The front and back of card to give people that walk in to our gym. There are a few things to say on the card. But it also needs to be designed in an attractive way. You can make some of the information bullett points or with icons or graphics. Please look at our website at https://ironleaftraining.com/ . The card will be 4" x 9"

Target Market(s)

High End Clientele who want to train in a private gym

Industry/Entity Type

Fitness

Font styles to use
Serif
Sans Serif
Other font styles liked:
• the same font Velto uses on the zelpad

Colors
F0912C
F2A743
F7CA91
FBE8D2
FDF5EE

Requirements
Must have
• A cool look

```html
<!DOCTYPE html>
<html lang="en">
<head>
<meta charset="utf-8">
<title>Ironleaf Private Training Studio – Information Card</title>
<link rel="stylesheet" href="https://fonts.googleapis.com/css2?family=Archivo+Black&family=Archivo:wght@700;800&display=swap">
<style>
  :root {
    --backdrop: #3d3d3d;
    --orange: #f0912c;
    --orange-deep: #ee8a25;
    --peach: #f7ca91;
    --white: #ffffff;
    --photo-dark: #3a2c26;
    --photo-mid: #7a6a62;
    --photo-light: #c9c2bd;
  }
  * { box-sizing: border-box; margin: 0; padding: 0; }
  html, body { width: 1200px; height: 1096px; overflow: hidden; background: var(--backdrop); }
  body { position: relative; font-family: "Archivo Black", "Archivo", sans-serif; color: var(--white); }

  .card { position: absolute; left: 34px; width: 1131px; overflow: hidden; }

  /* Front */
  .card-front { top: 36px; height: 501px; }
  .front-photo {
    position: absolute; inset: 0;
    background:
      radial-gradient(ellipse at 22% 30%, var(--photo-dark) 0%, rgba(58,44,38,0.85) 25%, transparent 45%),
      radial-gradient(ellipse at 60% 55%, var(--photo-light) 0%, transparent 45%),
      linear-gradient(110deg, var(--photo-mid) 0%, #a39690 45%, #8d807a 70%, #4e423d 100%);
  }
  .front-shade { position: absolute; inset: 0; background: linear-gradient(180deg, transparent 55%, rgba(30,24,22,0.45) 100%); }

  .brand { position: absolute; text-align: right; }
  .brand-name { display: flex; align-items: center; justify-content: flex-end; gap: 12px; font-family: "Archivo", sans-serif; font-weight: 800; color: var(--white); letter-spacing: 1px; line-height: 1; }
  .brand-mark { display: inline-block; background: var(--white); }
  .brand-tag { font-family: "Archivo", sans-serif; font-weight: 800; letter-spacing: 5px; line-height: 1; }

  .brand-front { right: 51px; top: 112px; }
  .brand-front .brand-name { font-size: 74px; }
  .brand-front .brand-mark { width: 22px; height: 22px; }
  .brand-front .brand-tag { font-size: 17px; margin-top: 16px; letter-spacing: 6px; }

  .front-headline { position: absolute; right: 51px; top: 380px; text-align: right; font-size: 42px; line-height: 42px; letter-spacing: 0.5px; text-transform: uppercase; }
  .front-url { position: absolute; right: 51px; top: 470px; font-size: 19px; line-height: 1; }

  /* Back */
  .card-back { top: 566px; height: 500px; background: var(--orange); }
  .goals-band { height: 125px; display: flex; align-items: center; justify-content: center; text-align: center; font-size: 29px; line-height: 37px; letter-spacing: 0.5px; text-transform: uppercase; }
  .promise-band { height: 97px; background: var(--white); color: var(--orange); display: flex; align-items: center; justify-content: center; text-align: center; font-size: 23px; line-height: 30px; text-transform: uppercase; }

  .rates { position: absolute; left: 35px; top: 248px; }
  .rates-title { font-size: 56px; line-height: 1; color: var(--peach); margin-left: 7px; letter-spacing: -1px; }
  .rate-row { display: flex; align-items: baseline; height: 61px; margin-top: 0; }
  .rates-title + .rate-row { margin-top: 10px; }
  .rate-count { width: 36px; font-size: 50px; line-height: 1; }
  .rate-freq { width: 102px; font-size: 20px; }
  .rate-price { font-size: 56px; line-height: 1; letter-spacing: -1px; margin-right: 14px; }
  .rate-note { font-size: 19px; }

  .brand-back { right: 46px; top: 228px; }
  .brand-back .brand-name { font-size: 54px; }
  .brand-back .brand-mark { width: 16px; height: 16px; }
  .brand-back .brand-tag { font-size: 12px; margin-top: 10px; letter-spacing: 4px; }

  .partner-box { position: absolute; left: 714px; right: 0; top: 319px; height: 94px; background: var(--white); color: var(--orange); text-align: right; padding: 14px 28px 0 0; }
  .partner-price { font-size: 42px; line-height: 44px; }
  .partner-label { font-size: 22px; line-height: 26px; }
  .partner-detail { position: absolute; right: 28px; top: 428px; text-align: right; font-family: "Archivo", sans-serif; font-weight: 800; font-size: 14px; line-height: 23px; letter-spacing: 0.3px; }
</style>
</head>
<body>
  <section class="card card-front">
    <div class="front-photo" role="img" aria-label="Close-up photograph of a hand gripping a kettlebell handle during a gym workout"></div>
    <div class="front-shade"></div>
    <div class="brand brand-front">
      <div class="brand-name"><span class="brand-mark"></span>IRONLEAF</div>
      <div class="brand-tag">PRIVATE TRAINING STUDIO</div>
    </div>
    <h1 class="front-headline">A safe and individualized<br>approach to strength training</h1>
    <div class="front-url">WWW.IRONLEAFTRAINING.COM</div>
  </section>

  <section class="card card-back">
    <div class="goals-band">Build strength, increase flexibility, improve functional<br>and daily movements, train for an event, or weight loss</div>
    <div class="promise-band">We will tailor your training program<br>to the specific results you are looking for</div>

    <div class="rates">
      <div class="rates-title">RATES</div>
      <div class="rate-row"><span class="rate-count">1</span><span class="rate-freq">x week</span><span class="rate-price">$110</span><span class="rate-note">per session (60 min.)</span></div>
      <div class="rate-row"><span class="rate-count">2</span><span class="rate-freq">x week</span><span class="rate-price">$85</span><span class="rate-note">per session (60 min.)</span></div>
      <div class="rate-row"><span class="rate-count">3</span><span class="rate-freq">x week</span><span class="rate-price">$80</span><span class="rate-note">per session (60 min.)</span></div>
    </div>

    <div class="brand brand-back">
      <div class="brand-name"><span class="brand-mark"></span>IRONLEAF</div>
      <div class="brand-tag">PRIVATE TRAINING STUDIO</div>
    </div>

    <div class="partner-box">
      <div class="partner-price">ADD $40</div>
      <div class="partner-label">FOR A PARTNERED SESSION</div>
    </div>
    <p class="partner-detail">A Partnered Session (2 people training together)<br>coming twice a week is $125 per session</p>
  </section>
</body>
</html>
```